Portfolio site - Need a basic WordPress or SquareSpace site

I need a portfolio site where I have the option to keep updating it on my own. Therefore, I'm guessing I need one that uses WordPress or SquareSpace. I just need a simple and elegant design. I'm a writer (scholarly, fiction and journalism).

Target Market(s)

Adult

Industry/Entity Type

Writer

Number of Pages Required

4 page

Font styles to use
Serif

Colors
b7a5cd
e667a6
85abd2

Requirements
Must have
• Easily updatable features. I'll have to publish links and small blurbs from time to time. And maybe the occasional image.
• Pages should be:
• Home
• Work
• Press
• Contact

```html
<!DOCTYPE html>
<html lang="en">
<head>
<meta charset="utf-8">
<title>Mirella Vantosh — Writer</title>
<link rel="stylesheet" href="https://fonts.googleapis.com/css2?family=Lora:ital,wght@0,400;0,700;1,400&family=Playfair+Display:ital@1&display=swap">
<style>
  :root {
    --lavender: #b7a5cd;
    --pink: #e667a6;
    --blue: #85abd2;
    --ink: #2d2d2d;
    --muted: #555555;
    --cover: #4a4a4a;
    --white: #ffffff;
    --serif: "Lora", Georgia, serif;
    --display: "Playfair Display", Georgia, serif;
  }
  * { box-sizing: border-box; margin: 0; padding: 0; }
  html, body { width: 667px; height: 1200px; overflow: hidden; background: var(--white); }
  body { position: relative; font-family: var(--serif); color: var(--ink); }

  .site-header { position: absolute; top: 0; left: 0; width: 667px; height: 111px; background: var(--lavender); border-bottom: 4px solid var(--pink); }
  .brand { position: absolute; top: 22px; width: 100%; text-align: center; font-size: 26px; color: var(--ink); font-weight: 400; }
  .main-nav { position: absolute; top: 78px; width: 100%; display: flex; justify-content: center; gap: 10px; }
  .main-nav a { font-size: 11px; color: var(--white); text-decoration: none; letter-spacing: 0.5px; padding: 4px 10px; }
  .main-nav a.is-active { background: var(--pink); }

  .hero { position: absolute; top: 115px; left: 0; width: 667px; height: 296px; background: linear-gradient(135deg, #d9d6d3 0%, #9a9591 45%, #3a3735 100%); }
  .hero-quote { position: absolute; left: 36px; top: 178px; width: 300px; color: var(--white); font-size: 17px; line-height: 1.3; }
  .hero-quote cite { display: block; font-size: 13px; font-style: italic; margin-top: 4px; }

  .section-title { position: absolute; width: 100%; text-align: center; font-family: var(--display); font-style: italic; color: var(--pink); font-size: 23px; }
  .news-title { top: 472px; }
  .releases-title { top: 766px; }

  .news-rule { position: absolute; top: 536px; height: 2px; background: var(--blue); }
  .quote-badge { position: absolute; top: 525px; width: 24px; height: 24px; border-radius: 50%; background: var(--blue); }

  .news-item { position: absolute; top: 572px; width: 170px; }
  .news-item h3 { font-size: 13px; font-weight: 400; margin-bottom: 8px; }
  .news-item p, .book p { font-size: 9.5px; line-height: 1.4; color: var(--muted); }
  .read-more { display: block; font-size: 9.5px; color: var(--pink); text-decoration: none; }

  .divider { position: absolute; top: 731px; left: 18px; width: 631px; height: 3px; background: var(--pink); }

  .book { position: absolute; top: 818px; width: 112px; }
  .book-cover { width: 100px; height: 137px; background: var(--cover); margin: 0 auto 16px; }
  .book h4 { font-size: 12px; font-weight: 400; text-align: center; margin-bottom: 8px; }
  .book p { text-align: left; }

  .site-footer { position: absolute; top: 1083px; left: 0; width: 667px; height: 117px; background: var(--blue); }
  .footer-brand { position: absolute; left: 22px; top: 48px; font-size: 14px; color: var(--white); }
  .copyright { position: absolute; left: 178px; top: 54px; font-size: 8px; color: var(--ink); }
  .social { position: absolute; right: 22px; top: 46px; display: flex; gap: 10px; }
  .social span { width: 20px; height: 20px; border-radius: 50%; background: #1f1f1f; }
</style>
</head>
<body>
  <header class="site-header">
    <div class="brand">Mirella Vantosh</div>
    <nav class="main-nav">
      <a class="is-active" href="#">HOME</a>
      <a href="#">WORK</a>
      <a href="#">PRESS</a>
      <a href="#">CONTACT</a>
    </nav>
  </header>

  <section class="hero" role="img" aria-label="Photo of a hand writing with a pen in a notebook">
    <blockquote class="hero-quote">
      To produce a mighty book, you must choose a mighty theme.
      <cite>~ Edwin Marlowe</cite>
    </blockquote>
  </section>

  <h2 class="section-title news-title">WHAT'S NEW?</h2>
  <div class="news-rule" style="left:24px;width:172px"></div>
  <div class="news-rule" style="left:246px;width:172px"></div>
  <div class="news-rule" style="left:468px;width:172px"></div>
  <svg class="quote-badge" style="left:98px" viewBox="0 0 24 24"><circle cx="12" cy="12" r="12" fill="#85abd2"/><path d="M7 14c0-3 1-4 3-5v2c-1 .5-1 1-1 2h1v3H7zM13 14c0-3 1-4 3-5v2c-1 .5-1 1-1 2h1v3h-3z" fill="#fff"/></svg>
  <svg class="quote-badge" style="left:320px" viewBox="0 0 24 24"><circle cx="12" cy="12" r="12" fill="#85abd2"/><path d="M7 14c0-3 1-4 3-5v2c-1 .5-1 1-1 2h1v3H7zM13 14c0-3 1-4 3-5v2c-1 .5-1 1-1 2h1v3h-3z" fill="#fff"/></svg>
  <svg class="quote-badge" style="left:542px" viewBox="0 0 24 24"><circle cx="12" cy="12" r="12" fill="#85abd2"/><path d="M7 14c0-3 1-4 3-5v2c-1 .5-1 1-1 2h1v3H7zM13 14c0-3 1-4 3-5v2c-1 .5-1 1-1 2h1v3h-3z" fill="#fff"/></svg>

  <article class="news-item" style="left:26px">
    <h3>TITLE 1</h3>
    <p>Fresh essays, notes from the archive and short fiction drafts appear here as they are finished, along with links to recent journal pieces and interviews.</p>
    <a class="read-more" href="#">READ MORE</a>
  </article>
  <article class="news-item" style="left:248px">
    <h3>TITLE 2</h3>
    <p>A new column on language and memory runs this season, with a reading list for each entry and a short reply to letters from readers.</p>
    <a class="read-more" href="#">READ MORE</a>
  </article>
  <article class="news-item" style="left:470px">
    <h3>TITLE 3</h3>
    <p>Upcoming talks, workshop dates and festival panels are listed below, together with notes on the research behind the next long project in progress.</p>
    <a class="read-more" href="#">READ MORE</a>
  </article>

  <div class="divider"></div>

  <h2 class="section-title releases-title">NEW RELEASES</h2>
  <article class="book" style="left:34px">
    <div class="book-cover" role="img" aria-label="Cover of Book Title 1"></div>
    <h4>Book Title 1</h4>
    <p>A quiet novel about two sisters, a river town and the letters they never sent.</p>
    <a class="read-more" href="#">READ MORE</a>
  </article>
  <article class="book" style="left:198px">
    <div class="book-cover" role="img" aria-label="Cover of Book Title 2"></div>
    <h4>Book Title 2</h4>
    <p>Collected essays on archives, exile and the strange habits of memory.</p>
    <a class="read-more" href="#">READ MORE</a>
  </article>
  <article class="book" style="left:362px">
    <div class="book-cover" role="img" aria-label="Cover of Book Title 3"></div>
    <h4>Book Title 3</h4>
    <p>Short stories set in harbour cities, told by workers, sailors and clerks.</p>
    <a class="read-more" href="#">READ MORE</a>
  </article>
  <article class="book" style="left:524px">
    <div class="book-cover" role="img" aria-label="Cover of Book Title 4"></div>
    <h4>Book Title 4</h4>
    <p>A scholarly study of reportage and the shaping of public record.</p>
    <a class="read-more" href="#">READ MORE</a>
  </article>

  <footer class="site-footer">
    <div class="footer-brand">Mirella Vantosh</div>
    <div class="copyright">Copyright 2016. All Rights Reserved.</div>
    <div class="social" aria-label="Social links">
      <span></span><span></span><span></span><span></span><span></span>
    </div>
  </footer>
</body>
</html>
```